Presentation Folder, Business Card, Letterhead and Envelope design

We are a dental clinic that will open in August and we are looking for a professional graphic designer to create our Business Card, Presentation Folder, Letterhead, Notepad and envelopes.

The brand Halden Dental must reflect a sense of quality and sophistication, marketed for middle-class consumers.
Our preference is for quality and refined materials, where less is more.
Attached the logo

```html
<!DOCTYPE html>
<html lang="en">
<head>
<meta charset="utf-8">
<title>Halden Dental Business Card</title>
<link href="https://fonts.googleapis.com/css2?family=Poppins:wght@400&display=swap" rel="stylesheet">
<style>
  :root {
    --backdrop: #aeb3b5;
    --paper: #f2f1ef;
    --brand-red: #7a1519;
    --edge-red: #5e1014;
    --ink-grey: #505356;
    --text-grey: #4a4a4a;
  }
  html, body {
    margin: 0;
    width: 1200px;
    height: 824px;
    overflow: hidden;
    background: var(--backdrop);
    font-family: "Poppins", sans-serif;
  }
  .sheet {
    width: 1200px;
    height: 824px;
    display: flex;
    align-items: center;
    justify-content: center;
    gap: 60px;
  }
  .card {
    position: relative;
    width: 500px;
    height: 286px;
    background: var(--paper);
    border-bottom: 4px solid var(--edge-red);
    box-sizing: border-box;
  }
  /* Contact side */
  .card-contact .holder {
    position: absolute;
    top: 34px;
    right: 40px;
    text-align: right;
  }
  .holder-name {
    margin: 0;
    font-size: 19px;
    font-weight: 400;
    color: var(--brand-red);
    letter-spacing: 0.3px;
  }
  .holder-title {
    margin: 2px 0 0;
    font-size: 13px;
    font-weight: 400;
    color: var(--text-grey);
  }
  .contact-list {
    position: absolute;
    left: 32px;
    right: 32px;
    bottom: 40px;
    display: flex;
    justify-content: space-between;
    align-items: flex-end;
    margin: 0;
    padding: 0;
    list-style: none;
  }
  .contact-item {
    display: flex;
    flex-direction: column;
    align-items: center;
    gap: 10px;
    font-size: 13px;
    color: var(--text-grey);
    letter-spacing: 0.3px;
    white-space: nowrap;
  }
  .contact-icon {
    width: 20px;
    height: 20px;
    background: var(--brand-red);
    display: flex;
    align-items: center;
    justify-content: center;
  }
  .contact-icon svg { width: 12px; height: 12px; }
  /* Brand side */
  .card-brand {
    display: flex;
    align-items: center;
    justify-content: center;
  }
  .brand-name {
    font-size: 34px;
    font-weight: 400;
    color: var(--ink-grey);
    letter-spacing: 1px;
  }
</style>
</head>
<body>
<main class="sheet">
  <section class="card card-contact">
    <div class="holder">
      <p class="holder-name">DANIEL REYES</p>
      <p class="holder-title">President</p>
    </div>
    <ul class="contact-list">
      <li class="contact-item">
        <span class="contact-icon">
          <svg viewBox="0 0 12 12" aria-hidden="true"><path d="M2.5 1.2l1.8 0 .8 2.4-1.2.9a6.5 6.5 0 0 0 3.6 3.6l.9-1.2 2.4.8v1.8c0 .6-.5 1.1-1.1 1.1A9.3 9.3 0 0 1 1.4 2.3c0-.6.5-1.1 1.1-1.1z" fill="#fff"/></svg>
        </span>
        555-214-7730
      </li>
      <li class="contact-item">
        <span class="contact-icon">
          <svg viewBox="0 0 12 12" aria-hidden="true"><rect x="1" y="2.5" width="10" height="7" fill="none" stroke="#fff" stroke-width="1.2"/><path d="M1 2.8l5 3.7 5-3.7" fill="none" stroke="#fff" stroke-width="1.2"/></svg>
        </span>
        info@haldendental.com
      </li>
      <li class="contact-item">
        <span class="contact-icon">
          <svg viewBox="0 0 12 12" aria-hidden="true"><circle cx="6" cy="6" r="4.6" fill="none" stroke="#fff" stroke-width="1.1"/><ellipse cx="6" cy="6" rx="2" ry="4.6" fill="none" stroke="#fff" stroke-width="1"/><path d="M1.4 6h9.2" stroke="#fff" stroke-width="1"/></svg>
        </span>
        www.haldendental.com
      </li>
    </ul>
  </section>
  <section class="card card-brand">
    <span class="brand-name">Halden Dental</span>
  </section>
</main>
</body>
</html>
```